Swimming Pool Supply Company Business Cards

We need business cards designed for company. These need to be easy to edit so that we can fill in names, titles, and contact info for each person who works here.

Dalton R. Pembry
Manager of Legal & Finance
J.L. Pembry, Incorporated

4837 Grelwood Avenue
Marlow Crossing, PA 19054

E. dalton@jlpembry.com
M. (215) 555-7193
O. (215) 555-4620

Contact Information for Business Card

Looking to upgrade current business cards with graphic that can be edited. Looking for fresh ideas for an age old industry.

Font styles to use
Serif
Sans Serif

Colors

Designer to choose colors to be used in the design.

Requirements
Must have
• Professional, fresh, unique but professional

```html
<!DOCTYPE html>
<html lang="en">
<head>
<meta charset="utf-8">
<title>J.L. Pembry, Incorporated — Business Card Samples</title>
<link rel="stylesheet" href="https://fonts.googleapis.com/css2?family=Alegreya+Sans:wght@400;500;700;800&display=swap">
<style>
  :root {
    --page: #ffffff;
    --ink: #111111;
    --card: #016a80;
    --card-edge: #0d1a1e;
    --mint: #8ff7e3;
    --text-light: #d8f6f3;
    --divider: #e6f7f5;
    --font: "Alegreya Sans", sans-serif;
  }
  * { margin: 0; padding: 0; box-sizing: border-box; }
  html, body { width: 1200px; height: 1200px; overflow: hidden; background: var(--page); }
  body { font-family: var(--font); color: var(--ink); }
  .canvas { position: relative; width: 1200px; height: 1200px; }
  .abs { position: absolute; line-height: 1; white-space: nowrap; }

  .sample-title { font-size: 62px; font-weight: 400; }
  .side-label { font-size: 20px; }

  .card {
    position: absolute;
    background: var(--card);
    border: 1.5px solid var(--card-edge);
    border-radius: 32px;
    overflow: hidden;
    color: var(--text-light);
  }
  .card .abs { color: var(--text-light); }
  .wordmark { color: var(--mint) !important; font-weight: 800; letter-spacing: 2px; }
  .tagline { color: var(--mint) !important; }
  .slot { position: absolute; background: var(--page); }
  .divider { position: absolute; background: var(--divider); width: 2px; }
  .icon { position: absolute; width: 12px; height: 12px; }
  .icon path, .icon rect, .icon circle { fill: none; stroke: var(--text-light); stroke-width: 1.4; }
  .icon .solid { fill: var(--text-light); stroke: none; }
  .icon .mint { fill: var(--mint); stroke: none; }
</style>
</head>
<body>
<div class="canvas">

  <!-- Sample 1 -->
  <div class="abs sample-title" style="left:476px; top:32px;">Sample 1</div>
  <div class="abs side-label" style="left:280px; top:136px;">Front</div>
  <div class="abs side-label" style="left:868px; top:136px;">Back</div>

  <section class="card card-horizontal-front" style="left:54px; top:170px; width:520px; height:305px;">
    <div class="slot" style="left:513px; top:132px; width:7px; height:130px;"></div>
    <div class="abs wordmark" style="left:0; width:520px; text-align:center; top:38px; font-size:64px;">PEMBRY</div>
    <div class="abs" style="left:0; width:520px; text-align:center; top:100px; font-size:20px;">J.L. Pembry, Incorporated</div>

    <div class="abs" style="right:296px; top:156px; font-size:20px;">Dalton R. Pembry</div>
    <div class="abs" style="right:296px; top:183px; font-size:14px;">Manager of Legal &amp; Finance</div>
    <div class="divider" style="left:247px; top:160px; height:118px;"></div>

    <svg class="icon" style="left:270px; top:163px;" viewBox="0 0 12 12"><path d="M3 1 L5 3 L4 5 Q5 8 8 9 L9 8 L11 10 L9 11.5 Q2 9 1.5 2.5 Z"/></svg>
    <div class="abs" style="left:289px; top:160px; font-size:17px;">(215) 555-7193</div>
    <svg class="icon" style="left:270px; top:189px;" viewBox="0 0 12 12"><path class="solid" d="M1 4 Q6 0 11 4 L9.5 5.5 L8 4.5 L4 4.5 L2.5 5.5 Z M3 6 L9 6 L10.5 11 L1.5 11 Z"/></svg>
    <div class="abs" style="left:289px; top:186px; font-size:17px;">(215) 555-4620</div>
    <svg class="icon" style="left:270px; top:215px;" viewBox="0 0 12 12"><rect x="1" y="2.5" width="10" height="7"/><path d="M1 2.5 L6 6.5 L11 2.5"/></svg>
    <div class="abs" style="left:289px; top:212px; font-size:17px;">dalton@jlpembry.com</div>
    <svg class="icon" style="left:270px; top:240px;" viewBox="0 0 12 12"><path class="mint" d="M6 0.5 A3.8 3.8 0 0 1 9.8 4.3 Q9.8 7 6 11.5 Q2.2 7 2.2 4.3 A3.8 3.8 0 0 1 6 0.5 Z M6 2.8 A1.5 1.5 0 1 0 6 5.8 A1.5 1.5 0 1 0 6 2.8 Z"/></svg>
    <div class="abs" style="left:289px; top:237px; font-size:17px;">4837 Grelwood Avenue</div>
    <div class="abs" style="left:289px; top:257px; font-size:17px;">Marlow Crossing, PA 19054</div>
  </section>

  <section class="card card-horizontal-back" style="left:622px; top:170px; width:520px; height:305px;">
    <div class="slot" style="left:0; top:132px; width:7px; height:130px;"></div>
    <div class="abs wordmark" style="left:0; width:520px; text-align:center; top:94px; font-size:100px; letter-spacing:5px;">PEMBRY</div>
    <div class="abs tagline" style="left:0; width:520px; text-align:center; top:182px; font-size:21px;">Deep Enough to Trust, Clear Enough to Enjoy</div>
  </section>

  <!-- Sample 2 -->
  <div class="abs side-label" style="left:198px; top:561px;">Front</div>
  <div class="abs side-label" style="left:657px; top:561px;">Back</div>
  <div class="abs sample-title" style="left:877px; top:652px;">Sample 2</div>

  <section class="card card-vertical-front" style="left:62px; top:611px; width:329px; height:560px;">
    <svg class="icon" style="left:116px; top:34px; width:12px; height:14px;" viewBox="0 0 12 14"><circle class="mint" cx="6" cy="4" r="3.3"/><path class="mint" d="M0.5 13.5 Q1 8 6 8 Q11 8 11.5 13.5 Z"/></svg>
    <div class="abs" style="left:134px; top:30px; font-size:22px;">Dalton R. Pembry</div>
    <div class="abs" style="left:134px; top:56px; font-size:15px;">Manager of Legal &amp; Finance</div>

    <div class="abs wordmark" style="left:0; width:329px; text-align:center; top:186px; font-size:66px;">PEMBRY</div>
    <div class="abs" style="left:0; width:329px; text-align:center; top:258px; font-size:22px;">J.L. Pembry, Incorporated</div>

    <svg class="icon" style="left:46px; top:413px;" viewBox="0 0 12 12"><path d="M3 1 L5 3 L4 5 Q5 8 8 9 L9 8 L11 10 L9 11.5 Q2 9 1.5 2.5 Z"/></svg>
    <div class="abs" style="left:67px; top:408px; font-size:19px;">(215) 555-7193</div>
    <svg class="icon" style="left:46px; top:442px;" viewBox="0 0 12 12"><path class="solid" d="M1 4 Q6 0 11 4 L9.5 5.5 L8 4.5 L4 4.5 L2.5 5.5 Z M3 6 L9 6 L10.5 11 L1.5 11 Z"/></svg>
    <div class="abs" style="left:67px; top:437px; font-size:19px;">(215) 555-4620</div>
    <svg class="icon" style="left:46px; top:470px;" viewBox="0 0 12 12"><rect x="1" y="2.5" width="10" height="7"/><path d="M1 2.5 L6 6.5 L11 2.5"/></svg>
    <div class="abs" style="left:67px; top:465px; font-size:19px;">dalton@jlpembry.com</div>
    <svg class="icon" style="left:46px; top:497px;" viewBox="0 0 12 12"><path class="mint" d="M6 0.5 A3.8 3.8 0 0 1 9.8 4.3 Q9.8 7 6 11.5 Q2.2 7 2.2 4.3 A3.8 3.8 0 0 1 6 0.5 Z M6 2.8 A1.5 1.5 0 1 0 6 5.8 A1.5 1.5 0 1 0 6 2.8 Z"/></svg>
    <div class="abs" style="left:67px; top:492px; font-size:19px;">4837 Grelwood Avenue</div>
    <div class="abs" style="left:67px; top:514px; font-size:19px;">Marlow Crossing, PA 19054</div>
  </section>

  <section class="card card-vertical-back" style="left:477px; top:611px; width:329px; height:560px;">
    <div class="abs wordmark" style="left:179px; top:280px; width:0; height:0;">
      <span style="position:absolute; left:0; top:0; transform:translate(-50%,-50%) rotate(90deg); font-size:104px; letter-spacing:6px;">PEMBRY</span>
    </div>
    <div class="abs tagline" style="left:118px; top:280px; width:0; height:0;">
      <span style="position:absolute; left:0; top:0; transform:translate(-50%,-50%) rotate(90deg); font-size:22px;">Deep Enough to Trust, Clear Enough to Enjoy</span>
    </div>
  </section>

</div>
</body>
</html>
```